Brochure for a six month Life Transformation program for executives

I need a A4 brochure that will be physically printed out to give to prospective clients for a six month coaching, life transformation program. I have included here a video link that discusses the brief in detail.
https://www.vidtrellis.com/share/4b81e2f09c3d47a6b52e18d0a7f3c915

I've uploaded a file with logos and photos to include as well as a outline of each page.
Updates

Here is an updated video to show you what I'm liking what I don't like https://www.vidtrellis.com/share/e92d07b1a6f84c3098d5b7c1f4a26e08

Target Market(s)

35 - 55 male executives

Industry/Entity Type

Life Coaching

Requirements
Must have
• All the information in the outline
Nice to have
• icons, vector diagrams, the theme of transformation and revolution

```html
<!DOCTYPE html>
<html lang="en">
<head>
<meta charset="utf-8">
<title>Executive Life Transformation Brochure – Cover</title>
<link href="https://fonts.googleapis.com/css2?family=Oswald:wght@600;700&family=Work+Sans:wght@300;400&display=swap" rel="stylesheet">
<style>
  :root {
    --backdrop: #e6e6e8;
    --cover-deep: #2c3680;
    --cover-mid: #3f4ea0;
    --cover-light: #8f97c4;
    --ink-white: #f4f4f8;
    --accent-yellow: #e6e23a;
    --rule: rgba(255,255,255,0.85);
  }
  * { box-sizing: border-box; margin: 0; padding: 0; }
  html, body {
    width: 1200px;
    height: 859px;
    overflow: hidden;
    background: var(--backdrop);
  }
  .stage {
    position: relative;
    width: 1200px;
    height: 859px;
  }
  .cover {
    position: absolute;
    left: 317px;
    top: 30px;
    width: 566px;
    height: 800px;
    overflow: hidden;
    box-shadow: 0 14px 40px rgba(0,0,0,0.18);
  }
  .cover-photo {
    position: absolute;
    inset: 0;
    background:
      radial-gradient(ellipse 55% 45% at 78% 62%, rgba(190,198,232,0.55), transparent 70%),
      radial-gradient(ellipse 40% 60% at 40% 25%, rgba(150,160,215,0.35), transparent 70%),
      linear-gradient(160deg, var(--cover-mid) 0%, var(--cover-deep) 55%, var(--cover-mid) 80%, var(--cover-light) 100%);
  }
  .brand {
    position: absolute;
    top: 118px;
    right: 48px;
    display: flex;
    align-items: center;
    gap: 10px;
    font-family: "Work Sans", sans-serif;
    font-weight: 400;
    font-size: 13px;
    letter-spacing: 0.32em;
    text-transform: uppercase;
    color: var(--ink-white);
  }
  .brand-dot {
    width: 10px;
    height: 10px;
    border-radius: 50%;
    background: var(--ink-white);
  }
  .headline {
    position: absolute;
    left: 62px;
    top: 392px;
    font-family: "Oswald", sans-serif;
    font-weight: 700;
    font-size: 68px;
    line-height: 0.96;
    letter-spacing: -0.02em;
    color: var(--ink-white);
  }
  .headline .line { display: block; }
  .headline .line-accent { color: var(--accent-yellow); }
  .divider {
    position: absolute;
    left: 62px;
    top: 612px;
    width: 440px;
    height: 2px;
    background: var(--rule);
  }
  .tagline {
    position: absolute;
    left: 62px;
    top: 630px;
    width: 450px;
    font-family: "Work Sans", sans-serif;
    font-weight: 300;
    font-size: 15px;
    line-height: 1.4;
    color: var(--ink-white);
  }
</style>
</head>
<body>
  <main class="stage">
    <article class="cover">
      <div class="cover-photo" role="img" aria-label="Blue-toned photograph of an executive in suit and tie clenching his fist"></div>
      <div class="brand">
        <span class="brand-dot"></span>
        <span class="brand-name">Steadfast Shift</span>
      </div>
      <h1 class="headline">
        <span class="line">Your Life,</span>
        <span class="line">Your Potential,</span>
        <span class="line line-accent">Your Revolution</span>
      </h1>
      <div class="divider"></div>
      <p class="tagline">A six month life transformation program for overworked executives to restore life balance through health and fitness optimization while maintaining their high functioning career.</p>
    </article>
  </main>
</body>
</html>
```